Self promotion real estate banner advert

I need a revamp of my banner adverts for homeplotlisting.com.au. I need it to entice people to engage by requesting market data, or an appraisal. I also want them to know I am a writer and have a book available and I need to be positioned as an authority on selling real estate and on the local area. it should also promote my success. These are my old banners. Or you can check them out on homeplotlisting.com.au under the suburb East Fremantle WA 6158. They are animated banners but can only be gif files at or under 40KB

Target Market(s)

Home owners

Industry/Entity Type

Real Estate Agent

Number of Pages Required

1 page

Font styles to use
Sans Serif

Colors
ec1f27
000000
fee18a

Requirements
Must have
• movement to draw attention, an offer, call to action - must have company logo, use the corporate colours in the logo but can add an interesting flash of attention grabbing colour to make it stand out even more!
Nice to have
• Authority figure, trustworthy, results driven
Should not have
• too many words, no call to action, be too fast as the current banner is.

```html
<!DOCTYPE html>
<html lang="en">
<head>
<meta charset="utf-8">
<title>Elmridge banner set</title>
<link href="https://fonts.googleapis.com/css2?family=Nunito:wght@300;400;700;800&display=swap" rel="stylesheet">
<style>
  :root{
    --navy:#03030f;
    --gold:#a99a71;
    --red:#c1331d;
    --white:#ffffff;
    --sky-a:#7d98b0;
    --sky-b:#a9bccb;
    --sunset-a:#3a5878;
    --sunset-b:#d99a55;
    --garden-a:#5a7446;
    --garden-b:#9fb0bd;
  }
  *{box-sizing:border-box;margin:0;padding:0}
  html,body{width:1200px;height:1200px;overflow:hidden;background:#fff}
  body{position:relative;font-family:"Nunito",sans-serif}
  .banner{position:absolute;overflow:hidden;background:var(--navy)}
  .leaderboard{left:9px;width:728px;height:90px}
  .skyscraper{top:299px;width:160px;height:600px}
  .photo{position:absolute}
  .logo-panel{position:absolute;right:0;top:0;width:168px;height:90px;background:var(--navy);border-left:4px solid var(--gold)}
  .brand{display:block;text-align:center;font-family:"Nunito",sans-serif;font-weight:700;color:var(--gold);letter-spacing:1px}
  .logo-panel .brand{font-size:20px;line-height:24px;margin-top:12px}
  .cta-small{position:absolute;left:20px;top:48px;width:124px;height:32px;border-radius:16px;background:var(--red);color:var(--white);font-weight:800;font-size:13px;display:flex;align-items:center;justify-content:center}
  .headline{position:absolute;color:var(--white);font-weight:300;line-height:1.1}
  .headline b{font-weight:800}
  .red{color:var(--red)}
  .gold{color:var(--gold)}
  .sky-footer{position:absolute;left:0;bottom:0;width:160px;height:88px;border-top:5px solid var(--gold);background:var(--navy)}
  .sky-footer .brand{font-size:22px;line-height:28px;margin-top:27px}
  .cta-large{position:absolute;left:6px;top:438px;width:148px;height:48px;border-radius:24px;background:var(--red);border:3px solid var(--gold);color:var(--white);font-weight:800;font-size:16px;display:flex;align-items:center;justify-content:center}
  .center{text-align:center;left:0;width:100%}
</style>
</head>
<body>

<div class="banner leaderboard" style="top:8px">
  <div class="photo" role="img" aria-label="Smiling agent portrait against a cloudy sky with small illustrated houses" style="left:0;top:0;width:560px;height:90px;background:linear-gradient(90deg,var(--sky-a),var(--sky-b) 75%,#c9d8b8)"></div>
  <div class="headline" style="left:42px;top:12px;font-size:28px;line-height:32px">What’s <b>YOUR</b><br><b>Home <span class="red">Worth</span>?</b></div>
  <div class="logo-panel"><span class="brand">ELMRIDGE</span><div class="cta-small">FIND OUT NOW</div></div>
</div>

<div class="banner leaderboard" style="top:105px;background:var(--white)">
  <div class="photo" role="img" aria-label="Agent holding her book in front of a coastal sunset" style="left:300px;top:0;width:264px;height:90px;background:linear-gradient(180deg,var(--sunset-a),var(--sunset-b));clip-path:polygon(0 0,100% 0,100% 100%,32px 100%,14px 60%,4px 25%)"></div>
  <svg width="60" height="90" style="position:absolute;left:292px;top:0" aria-hidden="true"><path d="M10 0 Q20 60 42 90" fill="none" stroke="var(--navy)" stroke-width="4"/></svg>
  <div class="headline" style="left:0;width:306px;text-align:center;top:8px;line-height:24px">
    <div style="font-size:18px;color:var(--gold);font-weight:400"><b class="red">GET ADVICE</b> from Renowned</div>
    <div style="font-size:17px;color:var(--navy);font-weight:800">Real-Estate Marketer <span style="font-weight:400">&amp;</span> Writer</div>
    <div style="font-size:23px;color:var(--gold);font-weight:700;line-height:28px">MAREN HOLLOWAY</div>
  </div>
  <div class="logo-panel"><span class="brand">ELMRIDGE</span><div class="cta-small">LEARN MORE</div></div>
</div>

<div class="banner leaderboard" style="top:202px">
  <div class="photo" role="img" aria-label="Happy homeowner jumping beside a for sale sign" style="left:0;top:0;width:268px;height:90px;background:linear-gradient(90deg,var(--garden-a),var(--garden-b) 55%,#8d3b36)"></div>
  <svg width="20" height="90" style="position:absolute;left:262px;top:0" aria-hidden="true"><path d="M14 0 Q4 45 14 90" fill="none" stroke="var(--white)" stroke-width="3"/></svg>
  <div class="headline" style="left:268px;width:292px;text-align:center;top:15px;font-size:24px;line-height:30px">
    <div class="gold" style="font-weight:800">Unlock The Value</div>
    <div style="font-weight:400">of YOUR Home</div>
  </div>
  <div class="logo-panel"><span class="brand">ELMRIDGE</span><div class="cta-small">GET STARTED</div></div>
</div>

<div class="banner skyscraper" style="left:9px">
  <div class="photo" role="img" aria-label="Smiling agent portrait under a cloudy sky with small illustrated houses" style="left:0;top:0;width:160px;height:512px;background:linear-gradient(180deg,var(--sky-a),var(--sky-b) 55%,#4a4d58)"></div>
  <div class="headline center" style="top:76px;font-size:29px;line-height:36px">What’s<br><b>YOUR</b><br><b>Home</b><br><b><span class="red">Worth</span>?</b></div>
  <div class="cta-large">FIND OUT NOW</div>
  <div class="sky-footer"><span class="brand">ELMRIDGE</span></div>
</div>

<div class="banner skyscraper" style="left:183px">
  <div class="photo" role="img" aria-label="Agent holding her book in front of a coastal sunset" style="left:0;top:230px;width:160px;height:282px;background:linear-gradient(180deg,var(--sunset-a),var(--sunset-b) 45%,#3a3940);clip-path:ellipse(210px 290px at 160px 290px)"></div>
  <svg width="160" height="80" style="position:absolute;left:0;top:222px" aria-hidden="true"><path d="M0 64 Q50 6 160 6" fill="none" stroke="var(--white)" stroke-width="4"/></svg>
  <div class="headline center" style="top:20px">
    <div class="red" style="font-size:18px;font-weight:800;line-height:24px">GET ADVICE</div>
    <div class="gold" style="font-size:17px;font-weight:400;line-height:22px">from Renowned</div>
    <div style="font-size:17px;font-weight:800;line-height:21px;margin-top:8px">Real-Estate<br>Marketer<br><span style="font-weight:400">&amp;</span> Writer</div>
    <div class="gold" style="font-size:22px;font-weight:700;line-height:29px;margin-top:8px">MAREN<br>HOLLOWAY</div>
  </div>
  <div class="cta-large">LEARN MORE</div>
  <div class="sky-footer"><span class="brand">ELMRIDGE</span></div>
</div>

<div class="banner skyscraper" style="left:357px">
  <div class="photo" role="img" aria-label="Happy homeowner jumping beside a sold property sign" style="left:0;top:0;width:160px;height:270px;background:linear-gradient(180deg,var(--garden-b),var(--garden-a) 75%,#6f8d3c)"></div>
  <svg width="160" height="30" style="position:absolute;left:0;top:252px" aria-hidden="true"><path d="M0 20 Q80 -8 160 20 L160 30 L0 30Z" fill="var(--navy)"/><path d="M0 20 Q80 -8 160 20" fill="none" stroke="var(--gold)" stroke-width="4"/></svg>
  <div class="headline center" style="top:276px;font-size:23px;line-height:29px">
    <div class="gold" style="font-weight:800">Unlock<br>The Value</div>
    <div style="font-weight:400">of<br>YOUR<br>Home</div>
  </div>
  <div class="cta-large">GET STARTED</div>
  <div class="sky-footer"><span class="brand">ELMRIDGE</span></div>
</div>

</body>
</html>
```